バリエーション多く提案していただき採用させていただきました。
自分の意図している事を非常に再現性高く提案していただきありがとうございます。
ご応募いただきありがとうございます。今後も募集しますので何卒宜しくお願いします。
恋愛学習コンテンツの動画サムネイル バナー作成の仕事の依頼
女性的 男性的
希望する色 特になし・その他 追記事項: カテゴリごとに色変えてほしい
特記事項
• 継続依頼あり
• 参考記事URL
https://palvento-mirai.example/korunade

```html
<!DOCTYPE html>
<html lang="ja">
<head>
<meta charset="UTF-8">
<title>会話の際「この人いいな」と思わせる方法3選 マッチングアプリ編</title>
<link rel="stylesheet" href="https://fonts.googleapis.com/css2?family=Noto+Sans+JP:wght@700;900&display=swap">
<style>
  :root {
    --ink: #111111;
    --paper: #ffffff;
    --band: rgba(20, 20, 20, 0.72);
    --band-light: rgba(40, 40, 40, 0.35);
    --photo-top: #2b2b2b;
    --photo-mid: #8a8a8a;
    --photo-low: #b9b9b9;
  }
  html, body {
    margin: 0;
    padding: 0;
    width: 1200px;
    height: 838px;
    overflow: hidden;
    background: var(--paper);
  }
  .thumbnail {
    position: relative;
    width: 1200px;
    height: 838px;
    overflow: hidden;
    font-family: "Noto Sans JP", sans-serif;
    color: var(--paper);
  }
  .scene-photo {
    position: absolute;
    inset: 0;
    background:
      linear-gradient(180deg, var(--photo-top) 0%, #555 6%, #9a9a9a 10%, var(--photo-mid) 40%, var(--photo-low) 70%, #9c9c9c 100%);
  }
  .overlay {
    position: absolute;
    inset: 0;
  }
  .headline {
    position: absolute;
    margin: 0;
    font-weight: 900;
    line-height: 1;
    letter-spacing: 0.01em;
    -webkit-text-stroke: 2px var(--ink);
    paint-order: stroke fill;
    text-shadow: 0 0 6px rgba(0,0,0,0.6);
  }
  .headline-lead {
    left: 24px;
    top: 330px;
    font-size: 54px;
  }
  .headline-main {
    left: 28px;
    top: 432px;
    font-size: 82px;
    letter-spacing: -0.02em;
  }
  .headline-tail {
    left: 480px;
    top: 538px;
    font-size: 60px;
  }
  .count-number {
    position: absolute;
    left: 848px;
    top: 372px;
    font-size: 168px;
    font-weight: 900;
    font-style: italic;
    line-height: 1;
    -webkit-text-stroke: 3px var(--ink);
    paint-order: stroke fill;
  }
  .count-suffix {
    position: absolute;
    left: 1008px;
    top: 420px;
    font-size: 112px;
    font-weight: 900;
    line-height: 1;
    -webkit-text-stroke: 3px var(--ink);
    paint-order: stroke fill;
  }
  .category-label {
    position: absolute;
    left: 702px;
    top: 712px;
    margin: 0;
    font-size: 50px;
    font-weight: 900;
    line-height: 1;
    color: var(--ink);
    letter-spacing: 0.01em;
  }
</style>
</head>
<body>
  <main class="thumbnail">
    <div class="scene-photo" role="img" aria-label="モノクロ写真：コンクリートの塀に並んで座る男女の脚元"></div>

    <svg class="overlay" width="1200" height="838" viewBox="0 0 1200 838" aria-hidden="true">
      <polygon points="0,318 1120,318 960,612 0,612" fill="var(--band)"/>
      <polygon points="1120,318 1200,318 1200,690 880,838 760,838" fill="var(--band-light)"/>
      <polygon points="720,700 1200,700 1200,800 670,800" fill="var(--paper)"/>
    </svg>

    <h1 class="headline headline-lead">会話の際</h1>
    <p class="headline headline-main">「この人いいな」と</p>
    <p class="headline headline-tail">思わせる方法</p>
    <span class="count-number">3</span>
    <span class="count-suffix">選</span>
    <p class="category-label">マッチングアプリ編</p>
  </main>
</body>
</html>
```